PPT template for BLM. Whiskey, wine, food, drink and music. Moments in time

Velvet Crane and Cellars. Liquor, food, music. Need slides for BLM, Liquor, food and music.

Think whiskey distillery meets music studio.

Its about moments in time with the people we love. Music, food and drink all play apart in the times we remember.

Target Market(s)

Investors

Industry/Entity Type

Entertainment

Colors

Designer to choose colors to be used in the design.

Requirements
Must have
• Utilize the logo or image without text in all slides.
Nice to have
• blank template pages with logo or just image. multiple versions I can utilize. Logo and image as backgrounds, logo in corner and so on. Logo in many colors, rainbow, nautilus shell. Golden ratio....
Should not have
• Do not need close ups of food. its about people and experiences and food is part of this. Think tables, parties, events, chocolate fountains, and so on

```html
<!DOCTYPE html>
<html lang="en">
<head>
<meta charset="utf-8">
<title>BLM – Presentation Template Overview</title>
<link href="https://fonts.googleapis.com/css2?family=Ubuntu:wght@400;500;700&family=Open+Sans:wght@400;600&display=swap" rel="stylesheet">
<style>
:root{
  --canvas:#000000;
  --paper:#ffffff;
  --green:#7cc11f;
  --green-light:#a8e02f;
  --green-pale:#dff3c0;
  --green-dark:#4b8b13;
  --forest:#0b2a0c;
  --ink:#1d1d1d;
  --grey:#8a8a8a;
  --grey-light:#c9c9c9;
}
*{margin:0;padding:0;box-sizing:border-box}
html,body{width:1064px;height:1200px;overflow:hidden;background:var(--canvas)}
body{position:relative;font-family:"Open Sans",Arial,sans-serif;color:var(--ink)}
.slide{position:absolute;background:var(--paper);overflow:hidden}
.slide.sm{width:248px;height:137px}
.slide.lg{width:503px;height:283px}
.slide .corner{position:absolute;right:-8px;bottom:-8px;width:18px;height:18px;border-radius:50%;background:var(--green)}
.slide .pager{position:absolute;left:5px;top:4px;display:flex;gap:2px}
.slide .pager i{width:3px;height:3px;border-radius:50%;background:var(--green)}
.lg .pager{left:8px;top:7px;gap:4px}
.lg .pager i{width:5px;height:5px}
.logo{position:absolute;right:6px;top:3px;z-index:5;display:flex;align-items:center;gap:2px;font-family:"Ubuntu",sans-serif;font-weight:500;font-size:5px;letter-spacing:.8px;color:var(--green-dark)}
.logo i{width:4px;height:4px;border-radius:50%;background:var(--green-dark)}
.lg .logo{right:10px;top:6px;font-size:8px;gap:3px}
.lg .logo i{width:6px;height:6px}
.photo{position:absolute}
.round{border-radius:50%}
.ring{border:2px solid var(--green-pale)}
.blob{position:absolute;border-radius:50%;background:var(--green-light)}
.ttl{position:absolute;font-family:"Ubuntu",sans-serif;font-weight:700;font-size:8.5px;color:var(--ink);white-space:nowrap}
.ttl.center{left:0;right:0;text-align:center}
.rule{position:absolute;height:1.5px;width:14px;background:var(--green)}
.tiny{position:absolute;font-size:3.6px;line-height:1.35;color:var(--grey)}
.tiny.center{text-align:center}
.label{position:absolute;font-size:3.8px;font-weight:600;color:var(--green)}
.bullet{position:absolute;width:11px;height:11px;border-radius:50%;background:var(--green)}
.bullet::after{content:"";position:absolute;inset:3px;border:1px solid #fff;border-radius:50%}

.hero{left:23px;top:22px;width:505px;height:283px;background:radial-gradient(ellipse at 30% 45%,#5c9e14 0%,#1d4a10 35%,var(--forest) 70%,#051405 100%)}
.hero .bottle{left:60px;top:12px;width:210px;height:268px;background:radial-gradient(ellipse at 45% 50%,rgba(170,240,60,.9) 0%,rgba(90,170,30,.55) 45%,rgba(20,60,15,0) 75%)}
.hero .brand{position:absolute;left:280px;width:200px;top:62px;text-align:center;color:#fff}
.hero .brand .mark{display:inline-flex;align-items:center;gap:7px;font-family:"Ubuntu",sans-serif;font-weight:500;font-size:34px;letter-spacing:6px}
.hero .brand .mark i{width:16px;height:16px;border-radius:50%;background:#fff;display:inline-block}
.hero .brand .sub{font-family:"Ubuntu",sans-serif;font-weight:400;font-size:7px;letter-spacing:3px;margin-top:4px}
.hero .lead{position:absolute;left:287px;width:186px;top:155px;font-size:6px;line-height:1.3;color:#e6f3dc;text-align:center}
.hero .btn{position:absolute;left:334px;top:191px;width:90px;height:20px;border:1.2px solid #fff;border-radius:3px;color:#fff;font-size:8.5px;text-align:center;line-height:17px}

.big-ttl{position:absolute;font-family:"Ubuntu",sans-serif;font-weight:700;color:var(--ink)}
.item-ttl{position:absolute;font-size:5.5px;font-weight:600;color:var(--green)}
.item-txt{position:absolute;font-size:4.2px;line-height:1.35;color:var(--grey)}
.big-bullet{position:absolute;width:26px;height:26px;border-radius:50%;background:var(--green);z-index:2}
.big-bullet::after{content:"";position:absolute;inset:8px;border:1.5px solid #fff;border-radius:3px}
</style>
</head>
<body>

<!-- Cover -->
<section class="slide hero" aria-label="Cover slide">
  <div class="photo bottle" role="img" aria-label="Whiskey bottle and glass glowing under warm party lights"></div>
  <div class="brand">
    <div class="mark"><i></i>BLM</div>
    <div class="sub">VELVET CRANE AND CELLARS</div>
  </div>
  <p class="lead">Moments in time with the people we love. Music, food and drink all play a part in the nights we remember most</p>
  <div class="btn">Lorem ipsum</div>
</section>

<!-- Original Single Malt -->
<section class="slide sm" style="left:536px;top:22px">
  <div class="pager"><i></i><i></i><i></i></div>
  <div class="logo"><i></i>BLM</div>
  <div class="blob" style="left:48px;top:5px;width:80px;height:80px"></div>
  <div class="blob" style="left:10px;top:95px;width:20px;height:20px"></div>
  <div class="photo round" style="left:10px;top:18px;width:120px;height:105px;border-radius:45%;background:radial-gradient(circle,#d9a24a 0%,#a8641f 45%,#5a3414 70%,rgba(255,255,255,0) 72%)" role="img" aria-label="Friends raising whiskey glasses around a barrel table"></div>
  <div class="ttl" style="left:144px;top:28px">Original Single Malt</div>
  <div class="rule" style="left:144px;top:41px;width:10px"></div>
  <div class="bullet" style="left:146px;top:51px"></div>
  <div class="label" style="left:162px;top:51px">Aged in oak casks</div>
  <div class="tiny" style="left:162px;top:57px;width:76px">Slow years in the cellar for a rich and smooth pour.</div>
  <div class="bullet" style="left:146px;top:85px"></div>
  <div class="label" style="left:162px;top:85px">Poured to share</div>
  <div class="tiny" style="left:162px;top:91px;width:76px">Raised together at every table we gather around.</div>
  <div class="corner"></div>
</section>

<!-- Original Taste -->
<section class="slide sm" style="left:792px;top:22px">
  <div class="pager"><i></i><i></i><i></i></div>
  <div class="logo"><i></i>BLM</div>
  <div class="photo round ring" style="left:14px;top:10px;width:84px;height:84px;background:radial-gradient(circle,#b88a4a,#5a3a22 60%,#2a1f18)" role="img" aria-label="Guests at a candlelit dinner party"></div>
  <div class="photo round ring" style="left:103px;top:78px;width:50px;height:50px;background:radial-gradient(circle,#8a6a3a,#2d2418)" role="img" aria-label="Chocolate fountain at an event"></div>
  <div class="photo round ring" style="left:167px;top:70px;width:56px;height:56px;background:radial-gradient(circle,#9a7a5a,#3f3226)" role="img" aria-label="Whiskey tasting among friends"></div>
  <div class="ttl" style="left:118px;top:18px">Original Taste</div>
  <div class="rule" style="left:118px;top:30px;width:10px"></div>
  <div class="tiny" style="left:118px;top:36px;width:112px">Good drink brings people together. Every pour here is made to be shared around a long table.</div>
  <div class="corner"></div>
</section>

<!-- Enjoy Each Note -->
<section class="slide sm" style="left:536px;top:167px">
  <div class="pager"><i></i><i></i><i></i></div>
  <div class="logo"><i></i>BLM</div>
  <div class="blob" style="left:25px;top:6px;width:24px;height:24px"></div>
  <div class="blob" style="left:70px;top:95px;width:30px;height:30px"></div>
  <div class="photo round ring" style="left:12px;top:22px;width:100px;height:100px;background:radial-gradient(circle,#c8904a,#6a3a2a 60%,#241a22)" role="img" aria-label="Live band playing on a small studio stage"></div>
  <div class="ttl" style="left:132px;top:38px">Enjoy Each Note</div>
  <div class="rule" style="left:132px;top:50px;width:10px"></div>
  <div class="tiny" style="left:132px;top:56px;width:100px">Turn it up, pass the glasses and enjoy every moment with the people you love.</div>
  <div class="bullet" style="left:132px;top:88px;width:9px;height:9px"></div>
  <div class="bullet" style="left:146px;top:88px;width:9px;height:9px"></div>
  <div class="bullet" style="left:160px;top:88px;width:9px;height:9px"></div>
  <div class="corner"></div>
</section>

<!-- Shared Tables -->
<section class="slide sm" style="left:792px;top:167px">
  <div class="pager"><i></i><i></i><i></i></div>
  <div class="logo"><i></i>BLM</div>
  <div class="photo" style="left:-20px;top:-30px;width:150px;height:140px;border-radius:50%;background:radial-gradient(circle at 55% 55%,#9a6a3a,#4a3a2a 50%,#1f1a16)" role="img" aria-label="Long party table with guests and glasses"></div>
  <div class="ttl" style="left:147px;top:32px">Shared Tables</div>
  <div class="rule" style="left:147px;top:44px;width:10px"></div>
  <div class="tiny" style="left:147px;top:50px;width:90px">Long evenings, full glasses and loud laughter.</div>
  <div class="bullet" style="left:147px;top:73px"></div>
  <div class="label" style="left:163px;top:73px">Private events</div>
  <div class="tiny" style="left:163px;top:79px;width:72px">Parties planned around you.</div>
  <div class="bullet" style="left:147px;top:95px"></div>
  <div class="label" style="left:163px;top:95px">Tasting nights</div>
  <div class="tiny" style="left:163px;top:101px;width:72px">Cask pours with live music.</div>
  <div class="corner"></div>
</section>

<!-- The Best Moments -->
<section class="slide sm" style="left:23px;top:313px">
  <div class="pager"><i></i><i></i><i></i></div>
  <div class="logo"><i></i>BLM</div>
  <div class="ttl center" style="top:15px">The Best Moments</div>
  <div class="rule" style="left:117px;top:27px"></div>
  <div class="tiny" style="left:6px;top:40px;width:58px;text-align:right">Share a toast with old friends.</div>
  <div class="tiny" style="left:6px;top:60px;width:58px;text-align:right">Set the table for the crowd.</div>
  <div class="tiny" style="left:6px;top:82px;width:58px;text-align:right">Play the song you all know.</div>
  <div class="bullet" style="left:67px;top:38px;background:var(--green-dark)"></div>
  <div class="bullet" style="left:67px;top:58px;background:var(--green-dark)"></div>
  <div class="bullet" style="left:67px;top:80px;background:var(--green-dark)"></div>
  <div class="photo" style="left:89px;top:38px;width:70px;height:60px;background:linear-gradient(135deg,#2a1f18,#a0642a 50%,#3a2a1f)" role="img" aria-label="Friends toasting at a whiskey bar"></div>
  <div class="bullet" style="left:168px;top:38px;background:var(--green-light)"></div>
  <div class="bullet" style="left:168px;top:58px;background:var(--green-dark)"></div>
  <div class="bullet" style="left:168px;top:80px;background:var(--green-dark)"></div>
  <div class="tiny" style="left:183px;top:40px;width:56px">Pour slowly and savour it.</div>
  <div class="tiny" style="left:183px;top:60px;width:56px">Dance until the lights dim.</div>
  <div class="tiny" style="left:183px;top:82px;width:56px">Remember the night together.</div>
  <div class="tiny center" style="left:20px;top:112px;width:208px">Moments in time are made of music, food and drink shared with the ones we hold close.</div>
  <div class="corner"></div>
</section>

<!-- Our Team -->
<section class="slide sm" style="left:280px;top:313px">
  <div class="pager"><i></i><i></i><i></i></div>
  <div class="logo"><i></i>BLM</div>
  <div class="ttl center" style="top:9px">Our Team</div>
  <div class="rule" style="left:117px;top:21px"></div>
  <div class="tiny center" style="left:30px;top:25px;width:188px">The people who make every evening worth remembering.</div>
  <div class="photo round ring" style="left:22px;top:40px;width:52px;height:52px;background:radial-gradient(circle,#8a6a4a,#2f2418)" role="img" aria-label="Team member portrait in the distillery"></div>
  <div class="photo round ring" style="left:96px;top:40px;width:52px;height:52px;background:radial-gradient(circle,#6a6a7a,#22222e)" role="img" aria-label="Team member portrait in the music studio"></div>
  <div class="photo round ring" style="left:170px;top:40px;width:52px;height:52px;background:radial-gradient(circle,#bba99a,#6a5a4a)" role="img" aria-label="Team member portrait in the kitchen"></div>
  <div class="label" style="left:22px;top:102px;width:52px;text-align:center">Master Distiller</div>
  <div class="label" style="left:96px;top:102px;width:52px;text-align:center">Studio Lead</div>
  <div class="label" style="left:170px;top:102px;width:52px;text-align:center">Head Chef</div>
  <div class="tiny" style="left:22px;top:113px;width:52px;text-align:center;letter-spacing:1px;color:var(--green)">● ● ●</div>
  <div class="tiny" style="left:96px;top:113px;width:52px;text-align:center;letter-spacing:1px;color:var(--green)">● ● ●</div>
  <div class="tiny" style="left:170px;top:113px;width:52px;text-align:center;letter-spacing:1px;color:var(--green)">● ● ●</div>
  <div class="corner"></div>
</section>

<!-- Choose Your Night -->
<section class="slide sm" style="left:23px;top:458px">
  <div class="pager"><i></i><i></i><i></i></div>
  <div class="logo"><i></i>BLM</div>
  <div class="ttl center" style="top:14px">Choose Your Night</div>
  <div class="rule" style="left:117px;top:26px"></div>
  <div class="tiny center" style="left:30px;top:30px;width:188px">Pick a pour, pull up a chair, and let the band play on.</div>
  <div class="photo" style="left:16px;top:48px;width:68px;height:42px;background:linear-gradient(135deg,#4a2f1c,#b07a3a)" role="img" aria-label="Whiskey tasting around oak barrels"></div>
  <div class="photo" style="left:90px;top:48px;width:68px;height:42px;background:linear-gradient(135deg,#5a3a2a,#c09a6a)" role="img" aria-label="Dinner party at a long table"></div>
  <div class="photo" style="left:164px;top:48px;width:68px;height:42px;background:linear-gradient(135deg,#1f1f3a,#8a5a3a)" role="img" aria-label="Live music session in a studio"></div>
  <div class="label" style="left:16px;top:94px;font-size:7px">1</div>
  <div class="label" style="left:90px;top:94px;font-size:7px">2</div>
  <div class="label" style="left:164px;top:94px;font-size:7px">3</div>
  <div class="tiny" style="left:24px;top:96px;width:60px">Cask tastings with friends.</div>
  <div class="tiny" style="left:98px;top:96px;width:60px">Feasts at the long table.</div>
  <div class="tiny" style="left:172px;top:96px;width:60px">Live sets and a late pour.</div>
  <div class="corner"></div>
</section>

<!-- Our Founder -->
<section class="slide sm" style="left:280px;top:458px">
  <div class="pager"><i></i><i></i><i></i></div>
  <div class="logo"><i></i>BLM</div>
  <div class="ttl center" style="top:9px">Our Founder</div>
  <div class="rule" style="left:117px;top:21px"></div>
  <div class="tiny center" style="left:30px;top:25px;width:188px">Built on a love of good company and long nights.</div>
  <div class="blob" style="left:14px;top:41px;width:70px;height:70px;background:var(--green-dark)"></div>
  <div class="blob" style="left:164px;top:41px;width:70px;height:70px;background:var(--green)"></div>
  <div class="photo round ring" style="left:62px;top:47px;width:58px;height:58px;border-color:#fff;background:radial-gradient(circle,#b89a8a,#5a4a3a)" role="img" aria-label="Founder portrait"></div>
  <div class="photo round ring" style="left:128px;top:47px;width:58px;height:58px;border-color:#fff;background:radial-gradient(circle,#c8d0d8,#8a9aa8)" role="img" aria-label="Co-founder portrait"></div>
  <div class="tiny" style="left:22px;top:66px;width:38px;color:#fff">Founder and host</div>
  <div class="tiny" style="left:190px;top:66px;width:40px;color:#fff">Co-founder and curator</div>
  <div class="corner"></div>
</section>

<!-- Master Distiller -->
<section class="slide lg" style="left:536px;top:313px">
  <div class="pager"><i></i><i></i><i></i></div>
  <div class="logo"><i></i>BLM</div>
  <div class="big-ttl" style="left:38px;top:66px;font-size:19px">Master Distiller</div>
  <div class="rule" style="left:38px;top:92px;width:22px;height:2px"></div>
  <div class="big-bullet" style="left:38px;top:110px"></div>
  <div class="item-ttl" style="left:71px;top:111px">Consectetur adipiscing</div>
  <div class="item-txt" style="left:71px;top:119px;width:140px">Lorem ipsum dolor sit amet, consectetur adipiscing elit, sed do eiusmod tempor incididunt ut labore.</div>
  <div class="big-bullet" style="left:38px;top:150px"></div>
  <div class="item-ttl" style="left:71px;top:151px">Consectetur adipiscing</div>
  <div class="item-txt" style="left:71px;top:159px;width:140px">Lorem ipsum dolor sit amet, consectetur adipiscing elit, sed do eiusmod tempor incididunt ut labore.</div>
  <div class="big-bullet" style="left:38px;top:189px"></div>
  <div class="item-ttl" style="left:71px;top:190px">Consectetur adipiscing</div>
  <div class="item-txt" style="left:71px;top:198px;width:140px">Lorem ipsum dolor sit amet, consectetur adipiscing elit, sed do eiusmod tempor incididunt ut labore.</div>
  <div class="blob" style="left:318px;top:108px;width:132px;height:132px"></div>
  <div class="blob" style="left:290px;top:74px;width:14px;height:14px;background:var(--green)"></div>
  <div class="blob" style="left:425px;top:30px;width:20px;height:20px"></div>
  <div class="blob" style="left:400px;top:58px;width:14px;height:14px;background:var(--green)"></div>
  <div class="photo" style="left:330px;top:6px;width:110px;height:277px;border-radius:50px 50px 0 0;background:linear-gradient(180deg,#f2f2f2 0%,#e8d8cc 25%,#f4f4f4 40%,#b02a2a 60%,#9a1f22 100%)" role="img" aria-label="Smiling distiller in white jacket and red apron, arms crossed"></div>
  <div class="big-bullet" style="left:290px;top:98px;width:34px;height:34px;background:var(--green-light)"></div>
  <div class="corner" style="width:26px;height:26px;right:-4px;bottom:-4px"></div>
</section>

<!-- Break Slide -->
<section class="slide lg" style="left:23px;top:603px;width:505px">
  <div class="pager"><i></i><i></i><i></i></div>
  <div class="logo"><i></i>BLM</div>
  <div class="blob" style="left:110px;top:118px;width:100px;height:100px"></div>
  <div class="blob" style="left:180px;top:225px;width:14px;height:14px;background:var(--green)"></div>
  <div class="photo" style="left:50px;top:34px;width:112px;height:249px;border-radius:50px 50px 0 0;background:linear-gradient(180deg,#f2f2f2 0%,#e6d2c2 22%,#2a4a9a 30%,#f4f4f4 34%,#e8e8e8 90%,#1a1f2e 100%)" role="img" aria-label="Smiling host in white jacket welcoming guests"></div>
  <div class="big-bullet" style="left:160px;top:72px;width:36px;height:36px;background:var(--green-light)"></div>
  <div class="big-ttl" style="left:212px;top:96px;font-size:40px;letter-spacing:2px">Break</div>
  <div class="big-ttl" style="left:258px;top:138px;font-size:32px;letter-spacing:2px;color:var(--green-light);font-weight:500">Slide</div>
  <div style="position:absolute;left:358px;top:108px;width:1px;height:74px;border-left:1px dashed var(--green)"></div>
  <div style="position:absolute;left:353px;top:103px;width:11px;height:11px;border:2px solid var(--green);border-radius:50%;background:#fff"></div>
  <div style="position:absolute;left:353px;top:176px;width:11px;height:11px;border:2px solid var(--green);border-radius:50%;background:#fff"></div>
  <div class="label" style="left:370px;top:105px;font-size:5px">12.00</div>
  <div class="label" style="left:370px;top:178px;font-size:5px">13.00</div>
  <div class="item-txt" style="left:370px;top:120px;width:120px">Lorem ipsum dolor sit amet, consectetur adipiscing elit, sed do eiusmod tempor incididunt ut labore et dolore magna aliqua. Ut enim ad minim veniam, quis nostrud exercitation ullamco laboris nisi ut aliquip ex ea commodo.</div>
  <div class="corner" style="width:26px;height:26px;right:-4px;bottom:-4px"></div>
</section>

<!-- Beautiful Mockup: phones -->
<section class="slide sm" style="left:536px;top:603px">
  <div class="pager"><i></i><i></i><i></i></div>
  <div class="logo"><i></i>BLM</div>
  <div class="blob" style="left:20px;top:45px;width:70px;height:70px;background:var(--green)"></div>
  <div class="photo" style="left:30px;top:20px;width:34px;height:70px;border-radius:6px;transform:rotate(-20deg);background:linear-gradient(160deg,#1a1a1a,#6a4a2a 40%,#2a2a2a)" role="img" aria-label="Phone showing an event booking app"></div>
  <div class="photo" style="left:70px;top:12px;width:34px;height:70px;border-radius:6px;transform:rotate(15deg);background:linear-gradient(160deg,#1a1a1a,#4a3a6a 40%,#2a2a2a)" role="img" aria-label="Phone showing a live music playlist"></div>
  <div class="ttl" style="left:126px;top:44px">Beautiful Mockup</div>
  <div class="rule" style="left:126px;top:56px;width:10px"></div>
  <div class="tiny" style="left:126px;top:62px;width:100px">Show the pours, the playlist and the night ahead.</div>
  <div style="position:absolute;left:126px;top:85px;width:20px;height:7px;background:var(--green)"></div>
  <div style="position:absolute;left:150px;top:85px;width:20px;height:7px;border:1px solid var(--grey-light)"></div>
  <div class="corner"></div>
</section>

<!-- Beautiful Mockup: devices -->
<section class="slide sm" style="left:792px;top:603px">
  <div class="pager"><i></i><i></i><i></i></div>
  <div class="logo"><i></i>BLM</div>
  <div class="blob" style="left:55px;top:22px;width:70px;height:70px"></div>
  <div class="photo" style="left:14px;top:34px;width:84px;height:54px;border:3px solid #222;background:linear-gradient(135deg,#d8b88a,#7a4a2a)" role="img" aria-label="Desktop screen showing the cellar website"></div>
  <div style="position:absolute;left:46px;top:88px;width:20px;height:8px;background:#bbb"></div>
  <div class="photo" style="left:94px;top:46px;width:38px;height:42px;border:2px solid #222;background:linear-gradient(135deg,#c8a88a,#5a3a2a)" role="img" aria-label="Tablet showing a tasting event"></div>
  <div class="photo" style="left:130px;top:56px;width:20px;height:32px;border:2px solid #222;background:linear-gradient(135deg,#8a7aa8,#3a2a4a)" role="img" aria-label="Phone showing a music session"></div>
  <div class="ttl" style="left:156px;top:36px">Beautiful Mockup</div>
  <div class="rule" style="left:156px;top:48px;width:10px"></div>
  <div class="tiny" style="left:156px;top:54px;width:84px">Every screen tells the story of a great night.</div>
  <div class="bullet" style="left:156px;top:76px;border-radius:2px"></div>
  <div class="tiny" style="left:171px;top:77px;width:68px">Bookings open all week.</div>
  <div class="bullet" style="left:156px;top:95px;border-radius:2px"></div>
  <div class="tiny" style="left:171px;top:96px;width:68px">Live sets every Friday.</div>
  <div class="corner"></div>
</section>

<!-- Beautiful Mockup: laptop -->
<section class="slide sm" style="left:536px;top:749px">
  <div class="pager"><i></i><i></i><i></i></div>
  <div class="logo"><i></i>BLM</div>
  <div class="ttl" style="left:12px;top:34px">Beautiful Mockup</div>
  <div class="rule" style="left:12px;top:46px;width:10px"></div>
  <div class="tiny" style="left:12px;top:52px;width:100px">A warm welcome on any screen for guests and investors.</div>
  <div class="tiny" style="left:10px;top:78px;width:30px;text-align:center;font-size:7px">▭</div>
  <div class="tiny" style="left:50px;top:78px;width:30px;text-align:center;font-size:7px">△</div>
  <div class="tiny" style="left:90px;top:78px;width:30px;text-align:center;font-size:7px;color:var(--green)">♪</div>
  <div class="tiny" style="left:10px;top:92px;width:30px;text-align:center">Cellar</div>
  <div class="tiny" style="left:50px;top:92px;width:30px;text-align:center">Dining</div>
  <div class="tiny" style="left:90px;top:92px;width:30px;text-align:center">Music</div>
  <div class="blob" style="left:210px;top:100px;width:34px;height:34px"></div>
  <div class="blob" style="left:128px;top:16px;width:18px;height:18px;background:var(--green)"></div>
  <div class="photo" style="left:140px;top:30px;width:102px;height:70px;border:3px solid #222;background:radial-gradient(circle,#a06a3a,#3a2a1f 60%,#1f1a2a)" role="img" aria-label="Laptop showing a recording studio session"></div>
  <div style="position:absolute;left:132px;top:100px;width:116px;height:4px;background:#bbb;border-radius:0 0 3px 3px"></div>
  <div class="corner"></div>
</section>

<!-- Beautiful Mockup: desktop -->
<section class="slide sm" style="left:792px;top:749px">
  <div class="pager"><i></i><i></i><i></i></div>
  <div class="logo"><i></i>BLM</div>
  <div class="ttl" style="left:18px;top:36px">Beautiful Mockup</div>
  <div class="rule" style="left:18px;top:48px;width:10px"></div>
  <div class="bullet" style="left:18px;top:56px"></div>
  <div class="tiny" style="left:34px;top:58px;width:80px">Private events and tastings.</div>
  <div class="bullet" style="left:18px;top:75px"></div>
  <div class="tiny" style="left:34px;top:77px;width:80px">Live music in the cellar.</div>
  <div class="bullet" style="left:18px;top:94px"></div>
  <div class="tiny" style="left:34px;top:96px;width:80px">Seasonal food menus.</div>
  <div class="blob" style="left:160px;top:14px;width:80px;height:80px"></div>
  <div class="photo" style="left:130px;top:18px;width:100px;height:70px;border:3px solid #222;transform:skewY(-6deg);background:linear-gradient(135deg,#2a1f18,#a0642a 55%,#3a2a1f)" role="img" aria-label="Desktop screen showing a whiskey tasting party"></div>
  <div style="position:absolute;left:170px;top:88px;width:16px;height:14px;background:#ccc"></div>
  <div style="position:absolute;left:158px;top:101px;width:40px;height:3px;background:#bbb"></div>
  <div class="bullet" style="left:222px;top:96px;width:14px;height:14px"></div>
  <div class="corner"></div>
</section>

<!-- Chart Diagram: area -->
<section class="slide sm" style="left:23px;top:894px">
  <div class="pager"><i></i><i></i><i></i></div>
  <div class="logo"><i></i>BLM</div>
  <div class="ttl center" style="top:9px">Chart Diagram</div>
  <div class="rule" style="left:117px;top:21px"></div>
  <div class="tiny center" style="left:30px;top:25px;width:188px">Growth across venues, bottles sold and nights booked.</div>
  <div style="position:absolute;left:22px;top:50px;width:28px;height:28px;background:var(--green-dark);color:#fff;font:700 6px Ubuntu,sans-serif;text-align:center;padding-top:6px">50%</div>
  <div style="position:absolute;left:56px;top:50px;width:28px;height:28px;background:var(--green-dark);color:#fff;font:700 6px Ubuntu,sans-serif;text-align:center;padding-top:6px">60%</div>
  <div style="position:absolute;left:22px;top:82px;width:28px;height:28px;background:var(--green);color:#fff;font:700 6px Ubuntu,sans-serif;text-align:center;padding-top:6px">70%</div>
  <div style="position:absolute;left:56px;top:82px;width:28px;height:28px;background:var(--green-light);color:#fff;font:700 6px Ubuntu,sans-serif;text-align:center;padding-top:6px">80%</div>
  <div class="tiny" style="left:150px;top:44px">Chart Title</div>
  <svg style="position:absolute;left:108px;top:50px" width="130" height="70" viewBox="0 0 130 70">
    <line x1="0" y1="60" x2="120" y2="60" stroke="#ddd" stroke-width=".5"/>
    <line x1="0" y1="40" x2="120" y2="40" stroke="#eee" stroke-width=".5"/>
    <line x1="0" y1="20" x2="120" y2="20" stroke="#eee" stroke-width=".5"/>
    <polygon points="5,32 30,22 55,30 70,40 95,28 120,16 120,42 90,44 70,44 40,38 5,34" fill="#a8e02f"/>
    <polygon points="5,34 40,38 70,44 90,44 120,42 95,36 70,40 55,30" fill="#5f9e1a"/>
  </svg>
  <div class="tiny" style="left:145px;top:124px;color:var(--green)">● ● ● ● ●</div>
  <div class="corner"></div>
</section>

<!-- Infographic: cubes -->
<section class="slide sm" style="left:280px;top:894px">
  <div class="pager"><i></i><i></i><i></i></div>
  <div class="logo"><i></i>BLM</div>
  <div class="ttl center" style="top:9px">Infographic Slide</div>
  <div class="rule" style="left:117px;top:21px"></div>
  <div class="tiny center" style="left:30px;top:25px;width:188px">Each block builds the next moment worth sharing.</div>
  <svg style="position:absolute;left:80px;top:44px" width="90" height="88" viewBox="0 0 90 88">
    <g fill="#4b8b13"><rect x="36" y="8" width="18" height="18"/></g>
    <g fill="#5f9e1a"><rect x="26" y="26" width="18" height="18"/><rect x="46" y="26" width="18" height="18"/></g>
    <g fill="#7cc11f"><rect x="16" y="44" width="18" height="18"/><rect x="36" y="44" width="18" height="18"/><rect x="56" y="44" width="18" height="18"/></g>
    <g fill="#a8e02f"><rect x="6" y="62" width="18" height="18"/><rect x="26" y="62" width="18" height="18"/><rect x="46" y="62" width="18" height="18"/><rect x="66" y="62" width="18" height="18"/></g>
    <g fill="#fff"><circle cx="45" cy="6" r="4"/><circle cx="35" cy="24" r="3"/><circle cx="55" cy="42" r="3"/><circle cx="45" cy="60" r="3"/></g>
  </svg>
  <div class="label" style="left:44px;top:40px;width:34px;text-align:right;color:var(--ink)">Gather</div>
  <div class="tiny" style="left:40px;top:46px;width:38px;text-align:right">Invite the people you love.</div>
  <div class="label" style="left:172px;top:40px;color:var(--ink)">Pour</div>
  <div class="tiny" style="left:172px;top:46px;width:40px">Open a bottle to share.</div>
  <div class="label" style="left:30px;top:72px;width:44px;text-align:right;color:var(--ink)">Cook</div>
  <div class="tiny" style="left:30px;top:78px;width:44px;text-align:right">Fill the table with food.</div>
  <div class="label" style="left:178px;top:72px;color:var(--ink)">Play</div>
  <div class="tiny" style="left:178px;top:78px;width:44px">Put the music on loud.</div>
  <div class="label" style="left:30px;top:104px;width:44px;text-align:right;color:var(--ink)">Dance</div>
  <div class="tiny" style="left:30px;top:110px;width:44px;text-align:right">Move until late at night.</div>
  <div class="label" style="left:178px;top:104px;color:var(--ink)">Remember</div>
  <div class="tiny" style="left:178px;top:110px;width:44px">Keep the moment forever.</div>
  <div class="corner"></div>
</section>

<!-- Chart Diagram: bars -->
<section class="slide sm" style="left:23px;top:1040px">
  <div class="pager"><i></i><i></i><i></i></div>
  <div class="logo"><i></i>BLM</div>
  <div class="ttl center" style="top:9px">Chart Diagram</div>
  <div class="rule" style="left:117px;top:21px"></div>
  <div class="tiny center" style="left:30px;top:25px;width:188px">Yearly results for every cellar and venue.</div>
  <div class="tiny" style="left:60px;top:44px">Chart Title</div>
  <svg style="position:absolute;left:12px;top:52px" width="120" height="72" viewBox="0 0 120 72">
    <line x1="8" y1="58" x2="116" y2="58" stroke="#ddd" stroke-width=".5"/>
    <g fill="#5f9e1a"><rect x="14" y="30" width="7" height="28"/><rect x="38" y="22" width="7" height="36"/><rect x="62" y="34" width="7" height="24"/><rect x="86" y="14" width="7" height="44"/></g>
    <g fill="#7cc11f"><rect x="22" y="38" width="7" height="20"/><rect x="46" y="30" width="7" height="28"/><rect x="70" y="26" width="7" height="32"/><rect x="94" y="10" width="7" height="48"/></g>
    <g fill="#a8e02f"><rect x="30" y="44" width="7" height="14"/><rect x="54" y="36" width="7" height="22"/><rect x="78" y="30" width="7" height="28"/><rect x="102" y="18" width="7" height="40"/></g>
  </svg>
  <div class="tiny" style="left:45px;top:126px;color:var(--green)">● ● ●</div>
  <div class="bullet" style="left:146px;top:52px"></div>
  <div class="label" style="left:162px;top:52px">Whiskey sales</div>
  <div class="tiny" style="left:162px;top:58px;width:72px">Steady rise each season.</div>
  <div class="bullet" style="left:146px;top:74px"></div>
  <div class="label" style="left:162px;top:74px">Event bookings</div>
  <div class="tiny" style="left:162px;top:80px;width:72px">Parties and private nights.</div>
  <div class="bullet" style="left:146px;top:96px"></div>
  <div class="label" style="left:162px;top:96px">Live sessions</div>
  <div class="tiny" style="left:162px;top:102px;width:72px">Music every weekend.</div>
  <div class="corner"></div>
</section>

<!-- Infographic: venn -->
<section class="slide sm" style="left:280px;top:1040px">
  <div class="pager"><i></i><i></i><i></i></div>
  <div class="logo"><i></i>BLM</div>
  <div class="ttl center" style="top:9px">Infographic Slide</div>
  <div class="rule" style="left:117px;top:21px"></div>
  <div class="tiny center" style="left:30px;top:25px;width:188px">Where music, food and drink meet to make memories.</div>
  <svg style="position:absolute;left:82px;top:44px" width="86" height="88" viewBox="0 0 86 88">
    <circle cx="43" cy="30" r="26" fill="#4b8b13" stroke="#fff" stroke-width="1.5"/>
    <circle cx="28" cy="56" r="26" fill="#5f9e1a" stroke="#fff" stroke-width="1.5" opacity=".95"/>
    <circle cx="58" cy="56" r="26" fill="#7cc11f" stroke="#fff" stroke-width="1.5" opacity=".9"/>
    <circle cx="43" cy="48" r="7" fill="#fff"/>
    <text x="43" y="18" font-size="4.5" fill="#fff" text-anchor="middle" font-family="Ubuntu,sans-serif">Music</text>
    <text x="20" y="66" font-size="4.5" fill="#fff" text-anchor="middle" font-family="Ubuntu,sans-serif">Food</text>
    <text x="66" y="66" font-size="4.5" fill="#fff" text-anchor="middle" font-family="Ubuntu,sans-serif">Drink</text>
  </svg>
  <div class="label" style="left:30px;top:50px;color:var(--ink)">Lorem ipsum</div>
  <div class="tiny" style="left:30px;top:56px;width:48px">Live sound to set the mood.</div>
  <div class="label" style="left:176px;top:50px;color:var(--ink)">Lorem ipsum</div>
  <div class="tiny" style="left:176px;top:56px;width:48px">Fine pours from our cellars.</div>
  <div class="label" style="left:30px;top:96px;color:var(--ink)">Lorem ipsum</div>
  <div class="tiny" style="left:30px;top:102px;width:48px">Plates to pass around.</div>
  <div class="label" style="left:176px;top:96px;color:var(--ink)">Lorem ipsum</div>
  <div class="tiny" style="left:176px;top:102px;width:48px">Friends around the table.</div>
  <div class="corner"></div>
</section>

<!-- Infographic: flower -->
<section class="slide lg" style="left:536px;top:894px">
  <div class="pager"><i></i><i></i><i></i></div>
  <div class="logo"><i></i>BLM</div>
  <div class="big-ttl" style="left:0;right:0;top:18px;text-align:center;font-size:15px;letter-spacing:1px">Infographic Slide</div>
  <div class="rule" style="left:228px;top:40px;width:46px;height:2px"></div>
  <div class="item-txt" style="left:90px;top:46px;width:323px;text-align:center">Lorem ipsum dolor sit amet, consectetur adipiscing elit, sed do eiusmod tempor incididunt ut labore et dolore magna aliqua. Ut enim ad minim veniam, quis nostrud exercitation ullamco.</div>
  <svg style="position:absolute;left:166px;top:82px" width="170" height="170" viewBox="0 0 170 170">
    <g fill="none" stroke-width="7">
      <circle cx="85" cy="42" r="30" stroke="#4b8b13"/>
      <circle cx="126" cy="72" r="30" stroke="#7cc11f"/>
      <circle cx="110" cy="120" r="30" stroke="#a8e02f"/>
      <circle cx="60" cy="120" r="30" stroke="#5f9e1a"/>
      <circle cx="44" cy="72" r="30" stroke="#3f7a10"/>
    </g>
    <g fill="none" stroke="#7cc11f" stroke-width="1.2">
      <line x1="85" y1="85" x2="85" y2="20"/><line x1="85" y1="85" x2="146" y2="66"/><line x1="85" y1="85" x2="122" y2="140"/><line x1="85" y1="85" x2="48" y2="140"/><line x1="85" y1="85" x2="24" y2="66"/>
    </g>
  </svg>
  <div class="item-ttl" style="left:56px;top:90px;width:124px;text-align:right">Replace your short text in here</div>
  <div class="item-txt" style="left:56px;top:98px;width:124px;text-align:right">This is a sample text. You can add your own text and description here to keep it simple.</div>
  <div class="item-ttl" style="left:326px;top:90px;width:124px">Replace your short text in here</div>
  <div class="item-txt" style="left:326px;top:98px;width:124px">This is a sample text. You can add your own text and description here to keep it simple.</div>
  <div class="item-ttl" style="left:24px;top:154px;width:124px;text-align:right">Replace your short text in here</div>
  <div class="item-txt" style="left:24px;top:162px;width:124px;text-align:right">This is a sample text. You can add your own text and description here to keep it simple.</div>
  <div class="item-ttl" style="left:358px;top:154px;width:124px">Replace your short text in here</div>
  <div class="item-txt" style="left:358px;top:162px;width:124px">This is a sample text. You can add your own text and description here to keep it simple.</div>
  <div class="item-ttl" style="left:56px;top:218px;width:124px;text-align:right">Replace your short text in here</div>
  <div class="item-txt" style="left:56px;top:226px;width:124px;text-align:right">This is a sample text. You can add your own text and description here to keep it simple.</div>
  <div class="item-ttl" style="left:326px;top:218px;width:124px">Replace your short text in here</div>
  <div class="item-txt" style="left:326px;top:226px;width:124px">This is a sample text. You can add your own text and description here to keep it simple.</div>
  <div class="corner" style="width:26px;height:26px;right:-4px;bottom:-4px"></div>
</section>

</body>
</html>
```